Internet Of Things brochure

Need to create a brochure with a common theme to our website and the last 2 pages of the attached file. All the contect is in the file that I have attached.
website www.norvalenetworks.com.au

Industry/Entity Type

Internet

```html
<!DOCTYPE html>
<html lang="en">
<head>
<meta charset="utf-8">
<title>Norvale Networks – Internet of Things Brochure</title>
<link rel="stylesheet" href="https://fonts.googleapis.com/css2?family=Exo+2:wght@400;500;600;700&display=swap">
<style>
:root{
  --canvas:#e9e9e9;
  --blue:#0b5fc1;
  --blue-bright:#0c6bd6;
  --blue-deep:#0a4aa3;
  --navy:#1b3d91;
  --navy-dark:#162f73;
  --footer-grey:#a7abb3;
  --white:#ffffff;
  --ink:#2a2f3a;
  --muted:#5a6270;
}
*{box-sizing:border-box;margin:0;padding:0}
html,body{width:1200px;height:2400px;overflow:hidden}
body{background:var(--canvas);font-family:"Exo 2",Arial,sans-serif;color:var(--white);position:relative}
.spread{position:absolute;left:112px;width:976px;display:flex;box-shadow:0 2px 6px rgba(0,0,0,.15)}
.page{position:relative;width:488px;height:100%;overflow:hidden}
.page + .page{border-left:1px solid rgba(255,255,255,.25)}
.abs{position:absolute}
.body-text{font-size:7px;line-height:1.4;text-align:justify}
.body-text p + p{margin-top:6px}
h2.page-title{font-weight:700;font-size:19px;line-height:1.1}
h3.section-title{font-weight:700;font-size:11px;line-height:1.2;margin:0 0 5px}
.bullet-list{list-style:none;font-size:7px;line-height:1.6}
.bullet-list li::before{content:"◊";margin-right:8px;font-size:6px}
.alpha-list{font-size:7px;line-height:1.4;text-align:justify;padding-left:14px}
.alpha-list li{margin-bottom:6px;list-style:lower-alpha}
.photo{position:absolute}
.band-dark{position:absolute;left:0;right:0;height:14px;background:var(--navy-dark)}
.footer{position:absolute;left:0;right:0;bottom:0;height:36px;background:var(--footer-grey);display:flex;align-items:center;padding:0 18px;gap:10px}
.brand{display:flex;align-items:center;gap:4px;font-weight:700;font-size:9px;color:var(--white)}
.brand-dot{width:12px;height:12px;border-radius:50%;background:var(--white)}
.badge{height:14px;background:rgba(255,255,255,.85)}
.badge.wide{width:44px}
.badge.square{width:14px}
.footer-divider{width:1px;height:18px;background:rgba(255,255,255,.7)}
.contact{margin-left:auto;text-align:right;font-size:5.5px;line-height:1.35;color:var(--white)}
.text-box{position:absolute;background:var(--blue-bright);padding:14px 16px;font-size:7.5px;line-height:1.4}
.smart-grid{position:absolute;left:0;right:0;top:384px;height:216px;background:var(--white);display:grid;grid-template-columns:repeat(3,1fr);padding:20px 30px;gap:14px 18px;color:var(--ink)}
.smart-item{display:flex;flex-direction:column}
.smart-head{display:flex;justify-content:space-between;align-items:flex-start;height:34px}
.smart-name{font-weight:600;font-size:7.5px;line-height:1.2;text-transform:uppercase}
.smart-icon{width:30px;height:30px;border-radius:50%}
.smart-desc{font-size:5.5px;line-height:1.4;color:var(--muted);margin-top:4px}
.commit-list{list-style:none;font-size:6.5px;line-height:1.35;color:var(--ink)}
.commit-list li{display:flex;align-items:center;gap:10px;margin-bottom:6px}
.commit-num{flex:none;width:14px;height:14px;border:1px solid var(--blue);border-radius:50%;color:var(--blue);font-size:8px;display:flex;align-items:center;justify-content:center}
</style>
</head>
<body>

<section class="spread" style="top:120px;height:656px">
  <article class="page" style="background:linear-gradient(160deg,var(--blue-bright),var(--blue-deep))">
    <svg class="abs" style="left:14px;top:28px" width="80" height="78" viewBox="0 0 80 78" aria-hidden="true">
      <rect x="2" y="2" width="60" height="46" fill="none" stroke="#fff" stroke-width="3"/>
      <rect x="2" y="2" width="60" height="9" fill="#fff"/>
      <circle cx="40" cy="48" r="27" fill="var(--blue)" stroke="#fff" stroke-width="3"/>
      <ellipse cx="40" cy="48" rx="11" ry="27" fill="none" stroke="#fff" stroke-width="2.5"/>
      <line x1="13" y1="48" x2="67" y2="48" stroke="#fff" stroke-width="2.5"/>
      <line x1="18" y1="35" x2="62" y2="35" stroke="#fff" stroke-width="2.5"/>
      <line x1="18" y1="61" x2="62" y2="61" stroke="#fff" stroke-width="2.5"/>
      <line x1="40" y1="21" x2="40" y2="75" stroke="#fff" stroke-width="2.5"/>
    </svg>
    <h2 class="page-title abs" style="left:100px;top:40px">Digital<br>Solutions</h2>
    <div class="body-text abs" style="left:100px;top:92px;width:140px">
      <p>Our digital solutions are varied – impacting all parts of the business model and are completely tailored to your business and your industry.</p>
      <p>We can cover the following scenarios (and more):</p>
    </div>
    <ol class="alpha-list abs" style="left:14px;top:171px;width:226px">
      <li>Introduce a digitally strategic business model, digitising operations and processes by leveraging cloud-based applications and mobile devices that digitise data collection and collation and supply chain processes</li>
      <li>Learning &amp; Development solutions that comprise an array of digitised approaches that are always available on the Cloud, can be built in minutes, are completely customisable, are easy to maintain and are mobile friendly</li>
      <li>Seamlessly integrating digital commerce into your existing brick &amp; mortar business quickly, strategically and cost effectively – helping you compete</li>
      <li>Creating targeted and measurable digital marketing campaigns that focus on increasing first-time and repeat sales and building long-term customer loyalty</li>
    </ol>
    <h2 class="abs" style="left:16px;top:400px;width:200px;font-size:15px;font-weight:700;line-height:1.1">How We're Helping Businesses Reimagine Their Business Through Digital</h2>
    <div class="abs" role="img" aria-label="Pictograms of people connected by a network" style="left:26px;top:464px;width:180px;height:34px;background:linear-gradient(90deg,rgba(255,255,255,.55),rgba(255,255,255,.35))"></div>
    <div class="abs" style="left:16px;top:520px;width:220px">
      <h3 class="section-title">Digital Commerce</h3>
      <ul class="bullet-list">
        <li>eCommerce</li><li>mCommerce</li><li>Digital payment integration</li><li>Logistics and Supply Chain Integration</li>
      </ul>
    </div>
    <div class="abs" style="left:252px;top:46px;width:222px">
      <h3 class="section-title">Digital Marketing</h3>
      <ul class="bullet-list">
        <li>SEO &amp; SEM</li><li>Marketing Insights &amp; Analytics</li><li>Responsive EDMs and Digital Campaigns</li><li>Digital CTA</li><li>Proximity Marketing</li>
      </ul>
      <h3 class="section-title" style="margin-top:14px">Digital Business Solutions</h3>
      <ul class="bullet-list">
        <li>Cloud ERP, CRM, SCM, HCM</li><li>IOT Integration to ERP, CRM, SCM</li><li>Digital Invoicing solutions</li><li>Any device ERP, CRM, SCM</li>
      </ul>
      <h3 class="section-title" style="margin-top:14px">Digital Learning</h3>
      <ul class="bullet-list">
        <li>Cloud LMS</li><li>Learning &amp; Development Solutions</li><li>Campus On Cloud</li>
      </ul>
      <h3 class="section-title" style="margin-top:14px">Request A Digital Discovery Work-shop</h3>
      <div class="body-text">
        <p>The Digital Discovery Workshop is a half-day opportunity for the Key Stakeholders of your business that allows Norvale Digital to identify and explore which areas of your business are best suited to a digital transformation. During this workshop you will also learn about the threats that the digital environment may pose to your business specifically, and the opportunities and possibilities that exist by applying digital solutions to your existing business. We also provide our clients with the opportunity to consider the overall strategy and actions needed within their organization to help them develop a competitive advantage inside the context of the ever-changing digital business environment. This analysis is relevant to all business types and industries.</p>
        <p>Interested in discovering your digital opportunities? Let's talk – 1300 555 010.</p>
      </div>
    </div>
    <div class="band-dark" style="top:606px"></div>
    <footer class="footer"><span class="brand"><span class="brand-dot"></span>Norvale</span><span class="footer-divider"></span><span class="badge wide"></span><span class="badge square"></span></footer>
  </article>

  <article class="page" style="background:var(--navy)">
    <h2 class="page-title abs" style="left:107px;top:118px">Smart Cities Initiative</h2>
    <div class="body-text abs" style="left:107px;top:150px;width:368px">
      <p>A smart city is an urban development vision to integrate multiple information and communication technology (ICT) and Internet of things (IoT) solutions in a secure fashion to manage a city's assets – the city's assets include, but are not limited to, local departments' information systems, schools, libraries, transportation systems, hospitals, power plants, water supply networks, waste management, law enforcement, and other community services. The goal of building a smart city is to improve quality of life by using urban informatics and technology to improve the efficiency of services and meet residents' needs. ICT allows city officials to interact directly with the community and the city infrastructure and to monitor what is happening in the city, how the city is evolving, and how to enable a better quality of life. Through the use of sensors integrated with real-time monitoring systems, data are collected from citizens and devices – then processed and analyzed. The information and knowledge gathered are keys to tackling inefficiency. Norvale Networks has the ability and smarts to push these solutions forward.</p>
      <p>Norvale Digital and Norvale Networks together with the partnership of Orvatel and Skyvane Cloud hosting all these systems, solutions and devices have never been easier and costeffective to deploy and capitalize on.</p>
    </div>
    <div class="smart-grid">
      <div class="smart-item"><div class="smart-head"><span class="smart-name">Smart<br>Governance</span><span class="smart-icon" role="img" aria-label="Speech bubbles icon" style="background:#2aa8e0"></span></div><p class="smart-desc">Interconnected e-democracy and across-city governance, including ICT-enabled services and interactions between public and private sectors.</p></div>
      <div class="smart-item"><div class="smart-head"><span class="smart-name">Smart<br>Economy</span><span class="smart-icon" role="img" aria-label="Shopping basket and globe icon" style="background:#e2463c"></span></div><p class="smart-desc">E-business and e-commerce, ICT-enabled manufacturing and delivery of services, as well as new products, new services and business models.</p></div>
      <div class="smart-item"><div class="smart-head"><span class="smart-name">Smart<br>Mobility</span><span class="smart-icon" role="img" aria-label="Bicycle icon" style="background:#f2c21b"></span></div><p class="smart-desc">ICT supported and integrated transport and logistics. Sustainable, safe and interconnected systems for public transport, cars, bicycles and pedestrians.</p></div>
      <div class="smart-item"><div class="smart-head"><span class="smart-name">Smart<br>Environment</span><span class="smart-icon" role="img" aria-label="Tree icon" style="background:#6cb33f"></span></div><p class="smart-desc">Smart energy including renewables, ICT-enabled energy grids, pollution control and monitoring, green buildings and green urban planning.</p></div>
      <div class="smart-item"><div class="smart-head"><span class="smart-name">Smart<br>People</span><span class="smart-icon" role="img" aria-label="Light bulb icon" style="background:#f0a23a"></span></div><p class="smart-desc">Those with e-skills, working in ICT-enabled roles, having access to education and training, human resources and capacity management.</p></div>
      <div class="smart-item"><div class="smart-head"><span class="smart-name">Smart<br>Living</span><span class="smart-icon" role="img" aria-label="Wireless signal icon" style="background:#ef7d22"></span></div><p class="smart-desc">ICT-enabled lifestyles, behaviour and consumption. Healthy and safe living in a culturally vibrant city with good quality housing.</p></div>
    </div>
    <div class="band-dark" style="top:606px"></div>
    <footer class="footer"><span class="brand"><span class="brand-dot"></span>Norvale</span><span class="footer-divider"></span><span class="badge wide"></span><span class="badge square"></span>
      <div class="contact">P: 1300 555 010<br>A: 41 Harbour Lane<br>Eastvale, NSW, 2199<br>W: www.norvalenetworks.com.au</div></footer>
  </article>
</section>

<section class="spread" style="top:888px;height:656px">
  <article class="page" style="background:var(--white)">
    <div class="abs" style="left:0;top:0;width:100%;height:56px;background:var(--blue)"></div>
    <h2 class="page-title abs" style="left:29px;top:24px">Smart Cities Initiative</h2>
    <div class="abs" role="img" aria-label="Layered smart city platform diagram showing city applications, IoT platform, cloud, shared network, city-wide access and devices and sensors" style="left:40px;top:104px;width:408px;height:290px;background:linear-gradient(180deg,#eef4fb,#cfe2f6 55%,#9fb4cf)"></div>
    <h3 class="abs" style="left:48px;top:418px;font-size:10px;font-weight:500;color:var(--blue)">How we help you get the most from your IoT and M2M solutions</h3>
    <p class="abs" style="left:48px;top:436px;width:260px;font-size:6px;line-height:1.4;color:var(--ink)">We are committed to delivering connected solutions that transform business productivity. We believe that IoT technology is changing the way businesses operate helping to drive operational efficiency, customer experience improvements and enabling new service-based revenue streams.</p>
    <p class="abs" style="left:48px;top:472px;font-size:6px;color:var(--ink)">Our commitment is demonstrated through:</p>
    <ol class="commit-list abs" style="left:48px;top:488px;width:270px">
      <li><span class="commit-num">1</span>Australia's largest mobile network, including the addition of narrowband IoT, providing greater coverage and a range of connectivity options to you.</li>
      <li><span class="commit-num">2</span>Ongoing investment in services, platforms and partners to enable innovative IoT solutions.</li>
      <li><span class="commit-num">3</span>Continued focus on helping businesses across all industries to understand and adopt IoT technology.</li>
      <li><span class="commit-num">4</span>Our uncompromising dedication to customer service.</li>
      <li><span class="commit-num">5</span>Our ability to deliver innovative end-to-end IoT solutions.</li>
    </ol>
    <div class="abs" role="img" aria-label="Illustration of a wireless signal, SIM card and connected vending machine" style="left:322px;top:437px;width:150px;height:124px;background:linear-gradient(135deg,#e3f1fb,#b9dcf4)"></div>
    <div class="abs" style="left:0;top:597px;width:100%;height:23px;background:var(--navy)"></div>
    <footer class="footer"><span class="brand"><span class="brand-dot"></span>Norvale</span><span class="footer-divider"></span><span class="badge wide"></span><span class="badge square"></span></footer>
  </article>

  <article class="page" style="background:var(--navy)">
    <div class="photo" role="img" aria-label="Photo of an engineer in a hard hat at a wind farm at dusk" style="left:0;top:0;width:488px;height:236px;background:linear-gradient(120deg,#3d4a57,#8a9aa6 55%,#c7ccd0)"></div>
    <div class="text-box" style="left:256px;top:136px;width:232px;height:108px">Innovate and transform your business with IoT solutions Put the Internet of Things (IoT) to work for you. Drive digital transformation across your business with end to end IoT solutions that can be tailored for any need, helping make informed decisions, optimise operations, reduce costs, and create new revenue streams.</div>
    <div class="abs" style="left:0;top:252px;width:488px;height:172px;background:var(--blue-bright)"></div>
    <div class="photo" role="img" aria-label="Photo of a tablet showing a fleet management dashboard" style="left:262px;top:252px;width:226px;height:160px;background:linear-gradient(135deg,#26313d,#5a7186 60%,#9bb0c0)"></div>
    <p class="abs" style="left:16px;top:302px;width:232px;font-size:7.5px;line-height:1.4">Remote monitoring Reduce manual, time-intensive processes when you connect and monitor your business devices and assets. Access, analyse, and use previously untapped data to automate business processes and trigger automatic alerts and actions, such as remote diagnostics, to help increase efficiencies and decrease costs.</p>
    <div class="photo" role="img" aria-label="Photo of cars driving on a dark road at night" style="left:0;top:424px;width:488px;height:182px;background:linear-gradient(100deg,#1a2030,#3a4658 50%,#202838)"></div>
    <div class="text-box" style="left:256px;top:478px;width:232px;height:118px">Connected vehicle Transform the driving experience while innovating automotive manufacturing with the Skyvane Connected Vehicle Platform. From Velia Assist and predictive services to cloud-enhanced advanced driver assistance systems, use industry-leading technology to create connected and differentiated driving experiences that increase customer loyalty and reveal new revenue opportunities.</div>
    <div class="band-dark" style="top:606px"></div>
    <footer class="footer"><span class="brand"><span class="brand-dot"></span>Norvale</span><span class="footer-divider"></span><span class="badge wide"></span><span class="badge square"></span>
      <div class="contact">P: 1300 555 010<br>A: 41 Harbour Lane<br>Eastvale, NSW, 2199<br>W: www.norvalenetworks.com.au</div></footer>
  </article>
</section>

<section class="spread" style="top:1648px;height:680px">
  <article class="page" style="background:var(--blue-bright)">
    <div class="photo" role="img" aria-label="Photo of a hand using a rugged tablet with a map application" style="left:168px;top:0;width:320px;height:216px;background:linear-gradient(135deg,#39414c,#7c8a97 55%,#b6c1c9);clip-path:polygon(14% 0,100% 0,100% 100%,0 100%)"></div>
    <p class="abs" style="left:24px;top:150px;width:200px;font-size:7.5px;line-height:1.4">Connected field service Detect, troubleshoot, and resolve issues remotely before your customers know there's a problem. When an issue escalates, automatically dispatch the best technician and tools to deliver a first-time fix.</p>
    <div class="abs" style="left:0;top:224px;width:488px;height:200px;background:var(--blue)"></div>
    <div class="photo" role="img" aria-label="Photo of a technician with ear protection checking industrial equipment" style="left:0;top:224px;width:290px;height:200px;background:linear-gradient(120deg,#6b5a3c,#b59a5c 50%,#4e5560);clip-path:polygon(0 0,100% 0,88% 100%,0 100%)"></div>
    <p class="abs" style="left:276px;top:296px;width:196px;font-size:7.5px;line-height:1.4;text-align:right">Predictive maintenance Anticipate your maintenance needs to prevent equipment failures and avoid unscheduled downtime. Analyse streaming data to quickly assess conditions, recognize warning signs, and preemptively service equipment before costly repairs are needed.</p>
    <div class="photo" role="img" aria-label="Photo of illuminated city skyscrapers at night" style="left:248px;top:424px;width:240px;height:200px;background:linear-gradient(160deg,#0d1320,#2c3346 55%,#4b5670);clip-path:polygon(16% 0,100% 0,100% 100%,0 100%)"></div>
    <p class="abs" style="left:24px;top:520px;width:220px;font-size:7.5px;line-height:1.4">Smart buildings Reduce costs, improve efficiencies, and increase occupant satisfaction and productivity using IoT. Gain actionable insights and control by connecting building devices and systems, collecting data, and running powerful analytics.</p>
    <div class="abs" style="left:0;top:624px;width:100%;height:20px;background:var(--navy)"></div>
    <footer class="footer"><span class="brand"><span class="brand-dot"></span>Norvale</span><span class="footer-divider"></span><span class="badge wide"></span><span class="badge square"></span></footer>
  </article>

  <article class="page" style="background:linear-gradient(170deg,var(--blue-bright),var(--blue-deep))">
    <svg class="abs" style="left:300px;top:22px" width="108" height="116" viewBox="0 0 108 116" aria-hidden="true">
      <g fill="none" stroke="#fff" stroke-width="3">
        <line x1="18" y1="16" x2="54" y2="40"/><line x1="54" y1="40" x2="42" y2="82"/><line x1="42" y1="82" x2="88" y2="100"/>
        <circle cx="14" cy="12" r="9"/><circle cx="56" cy="42" r="9"/><circle cx="40" cy="86" r="9"/><circle cx="92" cy="102" r="9"/>
      </g>
    </svg>
    <h2 class="abs" style="left:24px;top:54px;width:250px;font-size:17px;font-weight:700;line-height:1.1">EMBRACE DIGITAL<br>OR RISK BEING LEFT<br>BEHIND</h2>
    <div class="body-text abs" style="left:24px;top:130px;width:446px">
      <p>Does your business have the Digital DNA required to<br>succeed in the digital era?</p>
      <p>Embracing the new revolution in digital technology is more than just having an eCommerce website – it's about what is possible when every aspect of your business harnesses the power of digital innovation. When the sum of your business parts utilise digital and link together then your business can completely transform through being more effective, productive and automated.</p>
      <p>The way businesses operate has forever been changed by advancements in digital technology. Integrated systems allow for sophisticated e-Commerce, automated business operations, digital marketing, CRMs and learning &amp; development opportunities. These can be connected together so that digital-ready businesses have never been more agile, nimble and ready to compete and serve. These elements combined amount to a serious threat to those who utilise a 'traditional' business model and don't or can't adapt.</p>
      <p>Many enterprises have failed to adapt to this change. Through not integrating their business into the digital ecosystem, exposes them to the possibility of failing to properly engage with their customers.</p>
    </div>
    <h2 class="page-title abs" style="left:24px;top:334px">The Age of Digital<br>Disruption is Here</h2>
    <div class="body-text abs" style="left:24px;top:392px;width:318px">
      <p>The world's largest taxi firm, Tarvelo, owns no vehicles. The world's largest accommodation provider, Dwellorin, owns no real estate. The world's biggest phone companies, Vocallix and Chirrupa, own no telecommunication infrastructure. The world's most valuable retailer, Marqueto, carries no stock. The most popular media company, Plumora, creates no content. The world's largest movie house, Cinevanta, owns no cinemas. Something big has happened. It's called digital disruption.</p>
      <p>Creating and controlling the marketplace between the consumer and the provider of the goods or services is now the most valuable place to be. This is where risk is low, costs are slashed and profits are maximised. This digital revolution poses both a significant threat and a significant opportunity.</p>
      <p>To get a clearer picture of whether your business is digital ready, ask yourself: Is your business capable of responding quickly to digital threats? Are you doing all you can to compete in the digital business environment? Are you considering alternative business models and opportunities available through digitization?</p>
    </div>
    <svg class="abs" style="left:352px;top:412px" width="136" height="136" viewBox="0 0 136 136" aria-hidden="true">
      <g fill="none" stroke="#fff" stroke-width="6">
        <rect x="6" y="8" width="140" height="88" rx="4"/>
        <line x1="56" y1="98" x2="50" y2="122"/><line x1="96" y1="98" x2="102" y2="122"/>
        <line x1="36" y1="124" x2="116" y2="124"/>
      </g>
    </svg>
    <div class="band-dark" style="top:630px"></div>
    <footer class="footer"><span class="brand"><span class="brand-dot"></span>Norvale</span><span class="footer-divider"></span><span class="badge wide"></span><span class="badge square"></span>
      <div class="contact">P: 1300 555 010<br>A: 41 Harbour Lane<br>Eastvale, NSW, 2199<br>W: www.norvalenetworks.com.au</div></footer>
  </article>
</section>

</body>
</html>
```